Tractor Trailer & Van Graphics

Develop Graphics for our Vans, Tractor & Trailers, See our website www.quinleyforge.com for brand theme, I included a Brand Style Guide.
On the back doors of the trucks and van we want to highlight our core products, Packaging, Displays, Protective & E commerce, we are very proud of our sustainability efforts as we are 100% solar powered

Target Market(s)

Create Brand identify

Requirements
Must have
• Follow our brand guide line
Nice to have
• Logo. Locations Bullet point on back of trailer
Show Back door options
Show logo on tractor only
trailer show full. 1/2 coverage
Van full wrap

```html
<!DOCTYPE html>
<html lang="en">
<head>
<meta charset="utf-8">
<title>Quinleyforge Packaging – Trailer Side Graphic</title>
<link href="https://fonts.googleapis.com/css2?family=Montserrat:wght@500&family=Roboto+Condensed:ital,wght@0,700;1,700;1,800&display=swap" rel="stylesheet">
<style>
  :root {
    --red: #e2361c;
    --red-deep: #d92a1a;
    --orange: #f0641e;
    --orange-light: #f58a2a;
    --yellow: #ffd21a;
    --white: #ffffff;
    --grey: #6b6b6b;
    --page: #ffffff;
  }
  * { margin: 0; padding: 0; box-sizing: border-box; }
  html, body {
    width: 1200px; height: 800px; overflow: hidden;
    background: var(--page);
  }
  .trailer-graphic {
    position: absolute;
    left: 40px; top: 286px;
    width: 1120px; height: 228px;
    overflow: hidden;
    font-family: "Roboto Condensed", "Arial Narrow", sans-serif;
  }
  .trailer-graphic__bg { position: absolute; inset: 0; }

  .estimate-badge {
    position: absolute; left: 52px; top: 80px;
    display: flex; align-items: flex-start; gap: 2px;
  }
  .estimate-badge__label {
    background: var(--white);
    color: var(--red);
    font-style: italic; font-weight: 800;
    line-height: 0.9;
    padding: 3px 5px;
    transform: rotate(-8deg);
  }
  .estimate-badge__big { display: block; font-size: 17px; }
  .estimate-badge__small { display: block; font-size: 8px; letter-spacing: -0.2px; }
  .estimate-badge__icon { width: 30px; height: 30px; transform: rotate(-8deg); margin-top: -6px; }

  .contact-phone {
    position: absolute; left: 50px; top: 136px;
    color: var(--white);
    font-style: italic; font-weight: 800;
    font-size: 40px; letter-spacing: -1px;
    line-height: 1;
  }
  .contact-web {
    position: absolute; left: 50px; top: 176px;
    color: var(--yellow);
    font-style: italic; font-weight: 700;
    font-size: 20px; line-height: 1;
  }

  .product-showcase {
    position: absolute; left: 340px; top: 24px;
    width: 340px; height: 196px;
    background: linear-gradient(160deg, rgba(255,255,255,0.92), rgba(228,228,230,0.85));
    clip-path: polygon(24% 0, 100% 0, 100% 100%, 0 100%, 0 75%);
  }

  .brand {
    position: absolute; left: 722px; top: 26px;
    display: flex; align-items: center; gap: 14px;
  }
  .brand__mark {
    width: 54px; height: 54px; border-radius: 50%;
    background: var(--red);
  }
  .brand__text { display: flex; flex-direction: column; }
  .brand__name {
    font-family: "Montserrat", Arial, sans-serif;
    font-weight: 500; font-size: 31px;
    color: var(--red); letter-spacing: 0.5px; line-height: 1;
  }
  .brand__tagline {
    font-family: "Montserrat", Arial, sans-serif;
    font-weight: 500; font-size: 12px;
    color: var(--grey); letter-spacing: 11px;
    margin-top: 6px; padding-left: 50px;
  }

  .service-tag {
    position: absolute;
    width: 162px; height: 34px;
    display: flex; align-items: center; justify-content: center;
    color: var(--white);
    font-weight: 700; font-size: 20px; letter-spacing: -0.2px;
    background: linear-gradient(90deg, var(--orange) 0 6%, var(--red-deep) 6% 100%);
    clip-path: polygon(6% 0, 100% 0, 94% 100%, 0 100%);
  }
  .service-tag--packaging { left: 724px; top: 119px; }
  .service-tag--displays { left: 918px; top: 119px; }
  .service-tag--protective { left: 712px; top: 164px; }
  .service-tag--ecommerce { left: 910px; top: 164px; }
</style>
</head>
<body>
  <section class="trailer-graphic" aria-label="Trailer side graphic">
    <svg class="trailer-graphic__bg" width="1120" height="228" viewBox="0 0 1120 228" aria-hidden="true">
      <defs>
        <linearGradient id="panelRed" x1="0" y1="0" x2="1" y2="0">
          <stop offset="0" stop-color="#d9271b"/>
          <stop offset="0.55" stop-color="#e2401c"/>
          <stop offset="1" stop-color="#f0661e"/>
        </linearGradient>
      </defs>
      <rect width="1120" height="228" fill="#ffffff"/>
      <polygon points="0,0 705,0 644,228 0,228" fill="url(#panelRed)"/>
      <polygon points="330,0 420,0 360,228 270,228" fill="#ffffff" opacity="0.06"/>
      <polygon points="560,0 650,0 590,228 500,228" fill="#f58a2a" opacity="0.35"/>
    </svg>

    <div class="estimate-badge">
      <div class="estimate-badge__label">
        <span class="estimate-badge__big">FREE</span>
        <span class="estimate-badge__small">ESTIMATE</span>
      </div>
      <svg class="estimate-badge__icon" viewBox="0 0 30 30" aria-hidden="true">
        <path d="M4 3h22a3 3 0 0 1 3 3v15a3 3 0 0 1-3 3H12l-6 5v-5H4a3 3 0 0 1-3-3V6a3 3 0 0 1 3-3z" fill="#f58a2a"/>
        <path d="M11 8c-1 1-1 3 1 6s4 4 5.5 3.5l1.5-1.5-2.5-2-1.2 1c-1-.5-2.3-2-2.6-3l1-1.2-1.8-2.6z" fill="#ffffff"/>
        <path d="M17 8a5 5 0 0 1 4 4M17 5a8 8 0 0 1 7 7" stroke="#ffffff" stroke-width="1.6" fill="none" stroke-linecap="round"/>
      </svg>
    </div>

    <p class="contact-phone">1-555-014-2200</p>
    <p class="contact-web">www.quinleyforge.com</p>

    <div class="product-showcase" role="img" aria-label="White packaging boxes and retail display shelving units"></div>

    <div class="brand">
      <span class="brand__mark" aria-hidden="true"></span>
      <div class="brand__text">
        <span class="brand__name">QUINLEYFORGE</span>
        <span class="brand__tagline">PACKAGING</span>
      </div>
    </div>

    <span class="service-tag service-tag--packaging">PACKAGING</span>
    <span class="service-tag service-tag--displays">DISPLAYS</span>
    <span class="service-tag service-tag--protective">PROTECTIVE</span>
    <span class="service-tag service-tag--ecommerce">E-COMMERCE</span>
  </section>
</body>
</html>
```